NEW YORK Plumbing/utility company 10 year anniversary business card

Looking For simple back and front business card would like to include a few things in description
We offer 24/7 emergency service
residential
commercial
industrial
municipal
services offered
Plumbing
hydro excavation
hydro jetting
Well pumps
Sewer pumps
water mains
sewer mains

```html
<!DOCTYPE html>
<html lang="en">
<head>
<meta charset="utf-8">
<title>Ridgeline Water &amp; Sewer – Business Card</title>
<link rel="stylesheet" href="https://fonts.googleapis.com/css2?family=Montserrat:wght@400;500;600;700&display=swap">
<style>
  :root {
    --sky: #04b0f1;
    --navy: #00609e;
    --ink: #111111;
    --paper: #ffffff;
    --backdrop: #b3b3b3;
  }
  * { box-sizing: border-box; margin: 0; padding: 0; }
  html, body { width: 1000px; height: 1200px; overflow: hidden; }
  body {
    background: var(--backdrop);
    font-family: "Montserrat", Arial, sans-serif;
    color: var(--ink);
    position: relative;
  }
  .card {
    position: absolute;
    left: 51px;
    width: 898px;
    height: 538px;
    background: var(--paper);
    overflow: hidden;
  }
  .card--front { top: 44px; }
  .card--back { top: 618px; }
  .card__waves { position: absolute; inset: 0; width: 100%; height: 100%; }
  .wave--light { fill: var(--sky); }
  .wave--dark { fill: var(--navy); }

  /* Front */
  .brand {
    position: absolute;
    left: 75px;
    top: 178px;
    width: 370px;
    text-align: center;
    color: var(--navy);
    font-weight: 700;
    letter-spacing: 2px;
    text-transform: uppercase;
  }
  .brand__line { display: block; }
  .brand__line--main { font-size: 52px; line-height: 1.1; }
  .brand__line--sub { font-size: 26px; line-height: 1.5; letter-spacing: 4px; }

  .contact { position: absolute; left: 540px; top: 147px; }
  .contact__name { font-size: 24px; font-weight: 700; line-height: 1.2; }
  .contact__role { font-size: 24px; font-weight: 400; line-height: 1.2; margin-bottom: 8px; }
  .contact__list { list-style: none; }
  .contact__item {
    display: flex; align-items: center; gap: 9px;
    font-size: 22px; height: 39px;
  }
  .contact__icon { width: 25px; height: 25px; flex: none; }
  .contact__icon rect { fill: var(--navy); }
  .contact__icon .glyph { fill: none; stroke: #fff; stroke-width: 1.6; stroke-linecap: round; stroke-linejoin: round; }

  .social { position: absolute; left: 660px; top: 436px; display: flex; gap: 12px; }
  .social__tile { width: 47px; height: 47px; background: var(--navy); }

  /* Back */
  .tag {
    position: absolute; left: 0;
    display: flex; align-items: center;
    font-size: 25px; font-weight: 500; letter-spacing: 0.5px;
    padding-left: 30px;
    clip-path: polygon(0 0, calc(100% - 35px) 0, 100% 50%, calc(100% - 35px) 100%, 0 100%);
  }
  .tag--emergency { top: 142px; width: 595px; height: 65px; background: var(--navy); color: #fff; }
  .tag--services { top: 235px; width: 352px; height: 65px; background: var(--sky); color: var(--ink); }

  .sectors {
    position: absolute; left: 611px; top: 51px;
    width: 246px; height: 246px; border-radius: 50%;
    background: var(--sky);
    display: flex; flex-direction: column; justify-content: center; align-items: center;
    list-style: none;
    font-size: 25px; font-weight: 600; line-height: 35px; letter-spacing: 0.5px;
  }

  .services {
    position: absolute; top: 330px;
    list-style: none;
    font-size: 24px; font-weight: 600; letter-spacing: 0.5px;
  }
  .services--left { left: 159px; }
  .services--right { left: 523px; }
  .services li { height: 35.3px; display: flex; align-items: center; }
  .services li::before {
    content: ""; width: 8px; height: 8px; border-radius: 50%;
    background: var(--navy); margin-right: 12px; flex: none;
  }
</style>
</head>
<body>

<section class="card card--front" aria-label="Card front">
  <svg class="card__waves" viewBox="0 0 898 538" preserveAspectRatio="none" aria-hidden="true">
    <path class="wave--light" d="M0 0 H898 V64 C820 95 700 90 560 60 C420 30 300 10 180 25 C100 35 40 50 0 64 Z"/>
    <path class="wave--dark" d="M0 538 V474 C60 455 130 440 220 450 C350 465 550 520 720 515 C800 512 860 490 898 474 V538 Z"/>
  </svg>

  <h1 class="brand">
    <span class="brand__line brand__line--main">Ridgeline</span>
    <span class="brand__line brand__line--sub">Water &amp; Sewer</span>
  </h1>

  <div class="contact">
    <p class="contact__name">Your Name</p>
    <p class="contact__role">Manager</p>
    <ul class="contact__list">
      <li class="contact__item">
        <svg class="contact__icon" viewBox="0 0 25 25" aria-hidden="true"><rect width="25" height="25" rx="2"/><path class="glyph" d="M8 6 L10.5 6 L11.5 9.5 L10 11 C11 13.5 12 14.5 14 15.5 L15.5 14 L19 15 L19 17.5 C14 19 6 12 8 6 Z"/></svg>
        <span>123 444 555</span>
      </li>
      <li class="contact__item">
        <svg class="contact__icon" viewBox="0 0 25 25" aria-hidden="true"><rect width="25" height="25" rx="2"/><path class="glyph" d="M12.5 18 C9 13.5 8.5 12 8.5 10.5 A4 4 0 0 1 16.5 10.5 C16.5 12 16 13.5 12.5 18 Z"/><circle class="glyph" cx="12.5" cy="10.5" r="1.5"/><path class="glyph" d="M8 20 H17"/></svg>
        <span>789 Your Street Here</span>
      </li>
      <li class="contact__item">
        <svg class="contact__icon" viewBox="0 0 25 25" aria-hidden="true"><rect width="25" height="25" rx="2"/><rect class="glyph" x="5.5" y="7.5" width="14" height="10" style="fill:none"/><path class="glyph" d="M5.5 7.5 L12.5 13 L19.5 7.5 M5.5 17.5 L10.5 12 M19.5 17.5 L14.5 12"/></svg>
        <span>info@yourname.com</span>
      </li>
      <li class="contact__item">
        <svg class="contact__icon" viewBox="0 0 25 25" aria-hidden="true"><rect width="25" height="25" rx="2"/><circle class="glyph" cx="12.5" cy="12.5" r="6.5"/><ellipse class="glyph" cx="12.5" cy="12.5" rx="3" ry="6.5"/><path class="glyph" d="M6 12.5 H19 M7 9 H18 M7 16 H18"/></svg>
        <span>www.yourname.com</span>
      </li>
    </ul>
  </div>

  <div class="social" aria-hidden="true">
    <span class="social__tile"></span>
    <span class="social__tile"></span>
    <span class="social__tile"></span>
  </div>
</section>

<section class="card card--back" aria-label="Card back">
  <svg class="card__waves" viewBox="0 0 898 538" preserveAspectRatio="none" aria-hidden="true">
    <path class="wave--light" d="M0 0 H898 V63 C850 50 800 35 720 35 C580 35 400 85 240 84 C140 84 60 75 0 59 Z"/>
    <path class="wave--dark" d="M0 538 V473 C120 505 250 520 400 512 C600 500 800 440 898 473 V538 Z"/>
  </svg>

  <p class="tag tag--emergency">WE OFFER 24/7 EMERGENCY SERVICE</p>
  <h2 class="tag tag--services">SERVICES OFFERED</h2>

  <ul class="sectors">
    <li>RESIDENTIAL</li>
    <li>COMMERCIAL</li>
    <li>INDUSTRIAL</li>
    <li>MUNICIPAL</li>
  </ul>

  <ul class="services services--left">
    <li>PLUMBING</li>
    <li>HYDRO EXCAVATION</li>
    <li>HYDRO JETTING</li>
    <li>WELL PUMPS</li>
  </ul>
  <ul class="services services--right">
    <li>SEWER PUMPS</li>
    <li>WATER MAINS</li>
    <li>SEWER MAINS</li>
  </ul>
</section>

</body>
</html>
```